Harbour Stone Advisory Double Sided DL Flyer

We need a double sided flyer that we provide to a Real Estate agent for leeds. It should provide our basic services as well as a modern look and feel. The brochure should incorporate our Brand colors and have a graphic that centres around money and property. I have included a couple of pictures that we like (but have not yet purchased from PIXVAULT) as an indication of the type of picture we like.

WE need to also show the Harbour Stone Advisory brand and have our Phone / address's and email details.

Target Market(s)

Realestate clients (Property Investors)

Industry/Entity Type

Financial Planning

Requirements
Must have
• Picture on Front (maybe the logo on back)
• Please incorporate existing logo colours.

```html
<!DOCTYPE html>
<html lang="en">
<head>
<meta charset="utf-8">
<title>Harbour Stone Advisory – DL Flyer</title>
<link href="https://fonts.googleapis.com/css2?family=Saira:wght@400;500&family=Montserrat:wght@400;500;700&display=swap" rel="stylesheet">
<style>
  :root{
    --bg:#e4e4e4;
    --paper:#f4f4f4;
    --green:#8cc43f;
    --green-dark:#6fa52a;
    --ink:#1d1d1d;
    --muted:#333;
  }
  *{box-sizing:border-box;margin:0;padding:0}
  html,body{width:1200px;height:864px;overflow:hidden;background:var(--bg)}
  .canvas{position:relative;width:1200px;height:864px}
  .flyer{position:absolute;top:137px;width:280px;height:590px;background:var(--paper);overflow:hidden;font-family:'Montserrat',sans-serif;color:var(--ink)}
  .flyer--front{left:290px}
  .flyer--back{left:630px}
  .flyer__shapes{position:absolute;inset:0;width:280px;height:590px}
  .brand{position:absolute;top:38px;left:0;right:0;display:flex;align-items:center;justify-content:center;gap:8px}
  .brand__mark{width:14px;height:14px;background:var(--green)}
  .brand__name{font-family:'Saira',sans-serif;font-weight:500;font-size:16px;letter-spacing:.5px;color:var(--ink);text-transform:uppercase}
  .boxed-title{position:absolute;left:0;right:0;display:flex;justify-content:center}
  .boxed-title span{font-family:'Saira',sans-serif;border:1px solid var(--ink);border-left:6px solid var(--green);border-right:6px solid var(--green);background:#fff;padding:0 12px;line-height:1.15}
  .services-title{top:326px}
  .services-title span{font-size:23px}
  .intro{position:absolute;top:374px;left:0;right:0;text-align:center;color:var(--green);font-size:10.5px;line-height:19px}
  .service-list{position:absolute;top:425px;left:38px;list-style:none;font-size:9.2px;color:var(--muted)}
  .service-list li{display:flex;align-items:center;height:21px}
  .service-list li::before{content:"";width:6px;height:9px;border-left:3px solid var(--green);border-right:2px solid var(--green);margin-right:7px}
  .role{position:absolute;top:335px;left:38px;right:34px;text-align:center;font-family:'Saira',sans-serif;font-size:16px;border-bottom:1px solid var(--ink);padding-bottom:2px}
  .person{position:absolute;top:364px;left:0;right:0;display:flex;justify-content:center}
  .person span{font-family:'Saira',sans-serif;font-size:19px;color:var(--green-dark);border:1px solid var(--ink);border-top:none;border-bottom:none;padding:0 5px;line-height:1.2;position:relative}
  .address-title{top:444px}
  .address-title span{font-size:13px;padding:0 8px;border-left-width:4px;border-right-width:4px}
  .contact{position:absolute;top:474px;left:36px;list-style:none;font-size:8.8px;color:var(--muted)}
  .contact li{display:flex;align-items:flex-start;line-height:15px;margin-bottom:2px}
  .contact__icon{width:12px;height:12px;margin:1px 5px 0 0;flex:none}
  .contact__rule{width:1px;height:11px;background:var(--green);margin:2px 4px 0 0;flex:none}
</style>
</head>
<body>
<main class="canvas">

  <!-- Front side -->
  <section class="flyer flyer--front">
    <svg class="flyer__shapes" viewBox="0 0 280 590" aria-hidden="false">
      <defs>
        <linearGradient id="front-photo" x1="0" y1="0" x2="1" y2="1">
          <stop offset="0" stop-color="#d9cfc4"/>
          <stop offset=".45" stop-color="#eee9e2"/>
          <stop offset=".75" stop-color="#b9c9a0"/>
          <stop offset="1" stop-color="#8a9aa8"/>
        </linearGradient>
        <linearGradient id="band" x1="0" y1="0" x2="0" y2="1">
          <stop offset="0" stop-color="#a8d66a"/>
          <stop offset="1" stop-color="#7fb636"/>
        </linearGradient>
      </defs>
      <polygon points="0,116 280,74 280,82 0,124" fill="var(--green)"/>
      <polygon role="img" aria-label="Photo: hands holding a small wooden house beside growing stacks of coins with seedlings" points="0,124 280,82 280,262 0,292" fill="url(#front-photo)"/>
      <polygon points="0,292 280,262 280,272 0,306" fill="url(#band)"/>
      <polygon points="0,306 280,272 24,318 0,352" fill="var(--ink)"/>
      <polygon points="110,586 280,540 280,586" fill="var(--green)"/>
      <rect x="0" y="586" width="280" height="4" fill="var(--ink)"/>
    </svg>

    <div class="brand"><span class="brand__mark"></span><span class="brand__name">Harbour Stone Advisory</span></div>

    <h2 class="boxed-title services-title"><span>Services</span></h2>
    <p class="intro">Accountants and Financial<br>Advisors who specialise in</p>
    <ul class="service-list">
      <li>Negative Gearing &amp; Investment Properties</li>
      <li>Property &amp; Capital Gains Tax Minimisation</li>
      <li>Self-Managed Superannuation Funds (SMSF)</li>
      <li>Small Business &amp; Personal Taxation</li>
      <li>Investment Advice &amp; Risk Insurances</li>
    </ul>
  </section>

  <!-- Back side -->
  <section class="flyer flyer--back">
    <svg class="flyer__shapes" viewBox="0 0 280 590">
      <defs>
        <linearGradient id="back-photo" x1="0" y1="0" x2="0" y2="1">
          <stop offset="0" stop-color="#3f7a2a"/>
          <stop offset=".6" stop-color="#5e9a3a"/>
          <stop offset=".8" stop-color="#8a7458"/>
          <stop offset="1" stop-color="#6b563e"/>
        </linearGradient>
        <linearGradient id="band-back" x1="0" y1="0" x2="0" y2="1">
          <stop offset="0" stop-color="#a8d66a"/>
          <stop offset="1" stop-color="#7fb636"/>
        </linearGradient>
      </defs>
      <polygon points="0,116 280,74 280,82 0,124" fill="var(--green)"/>
      <polygon role="img" aria-label="Photo: watering can pouring onto a seedling in a jar of coins beside a small house model" points="0,124 280,82 280,262 0,292" fill="url(#back-photo)"/>
      <polygon points="0,292 280,262 280,272 0,306" fill="url(#band-back)"/>
      <polygon points="0,306 280,272 24,318 0,352" fill="var(--ink)"/>
      <polygon points="110,586 280,540 280,586" fill="var(--green)"/>
      <rect x="0" y="586" width="280" height="4" fill="var(--ink)"/>
    </svg>

    <div class="brand"><span class="brand__mark"></span><span class="brand__name">Harbour Stone Advisory</span></div>

    <p class="role">Advisor / Accountant</p>
    <p class="person"><span>Daniel Hartley</span></p>

    <h3 class="boxed-title address-title"><span>Address</span></h3>
    <ul class="contact">
      <li>
        <svg class="contact__icon" viewBox="0 0 12 12"><circle cx="6" cy="6" r="6" fill="var(--green)"/><path d="M6 2.6a2 2 0 0 0-2 2c0 1.5 2 4 2 4s2-2.5 2-4a2 2 0 0 0-2-2z" fill="#fff"/><circle cx="6" cy="4.6" r=".7" fill="var(--green)"/></svg>
        <span class="contact__rule"></span>
        <span>12 / 88 Shoreline Rd Bayview NSW 2104<br>3 / 17 Lakeside Pde Marlow NSW 2775<br>(By Appointment)</span>
      </li>
      <li>
        <svg class="contact__icon" viewBox="0 0 12 12"><circle cx="6" cy="6" r="6" fill="var(--green)"/><path d="M4 3.2l1.1 1.4-.6.8c.4.8 1 1.4 1.8 1.8l.8-.6 1.4 1.1-.7 1c-2.4-.4-4.2-2.2-4.6-4.6z" fill="#fff"/></svg>
        <span class="contact__rule"></span>
        <span>(02) 5550 1234</span>
      </li>
      <li>
        <svg class="contact__icon" viewBox="0 0 12 12"><circle cx="6" cy="6" r="6" fill="var(--green)"/><rect x="3" y="4" width="6" height="4.2" fill="#fff"/><path d="M3 4l3 2.3L9 4" stroke="var(--green)" stroke-width=".6" fill="none"/></svg>
        <span class="contact__rule"></span>
        <span>info@harbourstoneadvisory.com.au</span>
      </li>
    </ul>
  </section>

</main>
</body>
</html>
```